Hotel Company Personal Business Card

This is a hotel business, personal business card. Need it sleek, professional, and sharp looking. I have a design attached that we can work with. My turnaround time is April 8th. I would need the cards by then. One side only color, the other side all details. This is flexible depending on the designs you come up with. I would like a boutique, unique, modern type of touch to the business card. Memorable type of card that people will want to keep.

Target Market(s)

Business professionals

Industry/Entity Type

Hospitality/Hotels & Resorts

Contact Information for Business Card

Name, email, phone number, address, and company name. Anything unique

Font styles to use
Serif
Sans Serif

Colors

Designer to choose colors to be used in the design.

Requirements
Nice to have
• Neutral colors. Eye popping logo. Sleek design. Boutique feel. Hint of color.

```html
<!DOCTYPE html>
<html lang="en">
<head>
<meta charset="utf-8">
<title>Hotel Business Card</title>
<link rel="stylesheet" href="https://fonts.googleapis.com/css2?family=Montserrat:wght@300;500;600;700&display=swap">
<style>
  :root {
    --backdrop: #2b2c2f;
    --card-white: #ffffff;
    --navy: #17364f;
    --copper: #c98a5c;
    --copper-light: #e8b48c;
  }
  html, body {
    margin: 0;
    padding: 0;
    width: 1200px;
    height: 952px;
    overflow: hidden;
    background: var(--backdrop);
    font-family: "Montserrat", sans-serif;
  }
  .canvas {
    position: relative;
    width: 1200px;
    height: 952px;
  }
  .card {
    position: absolute;
    width: 540px;
    height: 309px;
    overflow: hidden;
    box-shadow: 0 10px 30px rgba(0,0,0,0.45);
  }
  .card--front {
    left: 50px;
    top: 470px;
    background: var(--card-white);
  }
  .card--back {
    left: 610px;
    top: 170px;
    background: var(--navy);
  }
  .ornament {
    position: absolute;
    width: 190px;
    height: 160px;
  }
  .card--front .ornament { background: radial-gradient(ellipse at center, rgba(232,180,140,0.45) 0%, rgba(232,180,140,0.15) 45%, rgba(255,255,255,0) 70%); }
  .card--back .ornament { background: radial-gradient(ellipse at center, rgba(201,138,92,0.55) 0%, rgba(201,138,92,0.18) 45%, rgba(23,54,79,0) 70%); }
  .ornament--top-left { left: -40px; top: -30px; }
  .ornament--bottom-right { right: -40px; bottom: -30px; }

  .identity {
    position: absolute;
    right: 300px;
    top: 96px;
    text-align: right;
  }
  .identity__name {
    margin: 0;
    font-weight: 500;
    font-size: 25px;
    letter-spacing: 0.5px;
    color: var(--navy);
    line-height: 1.1;
    white-space: nowrap;
  }
  .identity__name strong { font-weight: 700; }
  .identity__role {
    margin: 4px 0 0;
    font-weight: 300;
    font-size: 13px;
    color: var(--copper);
  }
  .divider {
    position: absolute;
    left: 256px;
    top: 62px;
  }
  .contact {
    position: absolute;
    left: 300px;
    top: 100px;
    margin: 0;
    padding: 0;
    list-style: none;
    color: var(--copper);
    font-weight: 600;
    font-size: 15px;
    line-height: 1.2;
    white-space: nowrap;
  }
  .contact li { margin-bottom: 16px; letter-spacing: 0.4px; }

  .brand {
    position: absolute;
    left: 0;
    top: 0;
    width: 100%;
    height: 100%;
  }
  .brand__rule {
    position: absolute;
    height: 2px;
    width: 115px;
    background: linear-gradient(90deg, var(--copper), var(--copper-light), var(--copper));
  }
  .brand__rule--top { left: 300px; top: 118px; }
  .brand__rule--bottom { left: 150px; top: 190px; }
  .brand__name {
    position: absolute;
    left: 0;
    right: 0;
    top: 140px;
    margin: 0;
    text-align: center;
    font-weight: 700;
    font-size: 21px;
    letter-spacing: 2px;
    color: var(--copper-light);
  }
</style>
</head>
<body>
<main class="canvas">
  <section class="card card--back" aria-label="Card back">
    <div class="ornament ornament--top-left" role="img" aria-label="Copper filigree swirl ornament"></div>
    <div class="ornament ornament--bottom-right" role="img" aria-label="Copper filigree swirl ornament"></div>
    <div class="brand">
      <span class="brand__rule brand__rule--top"></span>
      <p class="brand__name">COMPANY NAME</p>
      <span class="brand__rule brand__rule--bottom"></span>
    </div>
  </section>

  <section class="card card--front" aria-label="Card front">
    <div class="ornament ornament--top-left" role="img" aria-label="Copper filigree swirl ornament"></div>
    <div class="ornament ornament--bottom-right" role="img" aria-label="Copper filigree swirl ornament"></div>

    <div class="identity">
      <p class="identity__name">MARA <strong>ELLISON</strong></p>
      <p class="identity__role">Manager</p>
    </div>

    <svg class="divider" width="30" height="190" viewBox="0 0 30 190" aria-hidden="true">
      <line x1="15" y1="0" x2="15" y2="190" stroke="#17364f" stroke-width="2"/>
      <rect x="3" y="30" width="24" height="130" rx="12" fill="#17364f"/>
      <path d="M11 45 q-1 7 5 11 l2-2 -2-3 -2 1 q-2-2-2-5 l2-1 -1-3z" fill="#ffffff"/>
      <path d="M15 86 a5 5 0 0 1 5 5 c0 4-5 9-5 9 s-5-5-5-9 a5 5 0 0 1 5-5z" fill="#ffffff"/>
      <circle cx="15" cy="91" r="2" fill="#17364f"/>
      <rect x="8" y="131" width="14" height="10" fill="#ffffff"/>
      <polyline points="8,131 15,137 22,131" fill="none" stroke="#17364f" stroke-width="1.2"/>
    </svg>

    <ul class="contact">
      <li>#0178 415 366</li>
      <li>Harbor Lane, Old Town,<br>Number 24, 2045</li>
      <li>desk@maraguest.com</li>
    </ul>
  </section>
</main>
</body>
</html>
```